UI design for a mobile app that manages color schemes/pallettes

Should look cool, different, and modern.
The UI colors should not compete with pallette colors (as much as possible)
Features:
Currently looking for 3 pages/screens for the app: Browse through all palettes, view/edit a single palette, import
Features to include in the UI:
- View the list of color palettes (each list item includes a preview showing all colors in that color palette)
- View a particular color palette.
- Each displayed color should show:
- hex value
- rgb(255, 255, 255) value
- Name of pallete
- Button to copy the palette to a new pallette
- Sliders to change the properties (hue, saturation, value) or all colors in the palette at once
- Ability to add color
- Ability to remove color
- Switch background color that the pallete is displayed on: (black, mid gray, white, custom)
- A page that allows you to import palettes from a folder
Look and feel
Each slider illustrates characteristics of the customer's brand and the style your logo design should communicate.

```html
<!DOCTYPE html>
<html lang="en">
<head>
<meta charset="utf-8">
<title>Orbitone – Palette Manager Screens</title>
<link rel="stylesheet" href="https://fonts.googleapis.com/css2?family=Ubuntu:wght@400;500;700&display=swap">
<style>
:root{
  --stage:#5f7585;
  --screen:#ffffff;
  --ink:#0c1620;
  --ink-soft:#2b3440;
  --muted:#8a9099;
  --line:#e4e6ea;
  --row:#f3f4f6;
  --nav:#0b1620;
  --nav-icon:#2d79ab;
  --accent:#ff5a1f;
  --ok:#1fc24a;
  --bad:#e0241b;
}
*{box-sizing:border-box;margin:0;padding:0}
html,body{width:1200px;height:848px;overflow:hidden}
body{background:var(--stage);font-family:"Ubuntu",sans-serif;color:var(--ink);display:flex;align-items:center;justify-content:center;gap:40px}
.screen{width:340px;height:768px;background:var(--screen);border-radius:26px;overflow:hidden;position:relative;display:flex;flex-direction:column;box-shadow:0 18px 40px rgba(0,0,0,.25)}
.content{flex:1;padding:0 18px;display:flex;flex-direction:column}
.topbar{height:64px;display:flex;align-items:center;justify-content:space-between}
.brand{display:flex;align-items:center;gap:7px;font-size:15px;font-weight:500}
.brand-dot{width:12px;height:12px;border-radius:50%;background:var(--ink)}
.top-actions{display:flex;align-items:center;gap:10px}
.bg-switch{display:flex;gap:5px;padding:5px 8px;border-radius:12px;background:#fff;box-shadow:0 2px 8px rgba(0,0,0,.12)}
.bg-switch span{width:9px;height:9px;border-radius:50%;border:1px solid #9aa0a6}
.icon{display:block}
.page-title{font-size:17px;font-weight:500;display:flex;align-items:center;gap:12px;margin:8px 0 20px}

/* Browse */
.curated{display:flex;gap:10px;margin-bottom:26px}
.curated-card{flex:1;border-radius:6px;overflow:hidden;box-shadow:0 3px 10px rgba(0,0,0,.12)}
.band{height:16px;font-size:6.5px;color:#fff;padding-left:8px;display:flex;align-items:center;font-weight:500}
.curated-card p{font-size:8px;padding:8px;color:var(--ink-soft)}
.tabs{display:flex;gap:28px;font-size:14px;font-weight:500;color:var(--muted);margin-bottom:14px}
.tabs .active{color:var(--ink)}
.palette-item{border-radius:6px;box-shadow:0 3px 10px rgba(0,0,0,.09);padding:7px 7px 5px;margin-bottom:10px}
.swatches{display:flex;height:38px;border-radius:6px;overflow:hidden}
.swatches span{flex:1}
.item-meta{display:flex;justify-content:space-between;font-size:8px;color:var(--ink-soft);padding:6px 2px 0}

/* Palette detail */
.colour-row{height:64px;display:flex;align-items:center;justify-content:space-between;padding:0 14px;color:#fff;text-align:center;font-size:9px;line-height:1.5}
.colour-list{border-radius:6px;overflow:hidden;margin-bottom:10px}
.colour-row.faded{color:rgba(255,255,255,.8)}
.round-btn{width:22px;height:22px;border-radius:50%;border:1.3px solid currentColor;display:flex;align-items:center;justify-content:center}
.add-row{height:64px;border:1px solid var(--line);border-radius:6px;display:flex;align-items:center;justify-content:center;margin-bottom:14px}
.primary-btn{height:40px;background:var(--ink);color:#fff;border-radius:5px;display:flex;align-items:center;justify-content:center;gap:8px;font-size:12px;font-weight:500}

/* Import */
.upload{width:96px;height:96px;border-radius:50%;border:8px solid #d9dbdd;margin:14px auto 22px;display:flex;align-items:center;justify-content:center}
.upload-core{width:68px;height:68px;border-radius:50%;background:var(--ink);display:flex;align-items:center;justify-content:center}
.hint{font-size:9.5px;text-align:center;line-height:1.4;margin-bottom:24px;color:var(--ink-soft)}
.file-row{height:46px;background:var(--row);border-radius:5px;display:flex;align-items:center;padding:0 14px 0 10px;gap:12px;margin-bottom:5px}
.file-icon{width:25px;height:25px;border-radius:50%;background:var(--ink);display:flex;align-items:center;justify-content:center}
.file-info{flex:1;font-size:10px}
.file-info small{display:block;font-size:7px;color:var(--muted);margin-top:3px}
.status{width:16px;height:16px;border-radius:50%;display:flex;align-items:center;justify-content:center}
.status.ok{background:var(--ok)}.status.bad{background:var(--bad)}
.import .primary-btn{margin-top:22px}

/* Nav */
.tabbar{height:60px;background:var(--nav);display:flex;justify-content:space-around;align-items:center;color:var(--nav-icon)}
.tab{position:relative;display:flex;flex-direction:column;align-items:center}
.tab.home{color:#fff}
.tab.home::after{content:"";width:3px;height:3px;border-radius:50%;background:var(--accent);position:absolute;bottom:-6px}
.badge{position:absolute;top:-5px;right:-6px;width:11px;height:11px;border-radius:50%;background:var(--accent);color:#fff;font-size:7px;display:flex;align-items:center;justify-content:center}
</style>
</head>
<body>

<!-- Browse palettes -->
<section class="screen browse">
  <div class="content">
    <header class="topbar">
      <div class="brand"><span class="brand-dot"></span>Orbitone</div>
      <div class="top-actions">
        <div class="bg-switch" aria-label="Background colour">
          <span style="background:#111;border-color:#111"></span><span style="background:#fff"></span><span style="background:#888;border-color:#888"></span><span style="background:#f5dcc0"></span>
        </div>
        <svg class="icon" width="16" height="16" viewBox="0 0 16 16"><circle cx="8" cy="8" r="7" fill="var(--ink)"/><circle cx="8" cy="8" r="2.5" fill="#fff"/></svg>
        <svg class="icon" width="16" height="12" viewBox="0 0 16 12" stroke="var(--ink)" stroke-width="1.3"><path d="M0 2h16M0 6h16M0 10h16"/></svg>
      </div>
    </header>
    <h1 class="page-title">Curated Palette</h1>
    <div class="curated">
      <div class="curated-card">
        <div class="band" style="background:#2b2e4a"># 2B2E4A</div><div class="band" style="background:#e84545"># E84545</div><div class="band" style="background:#903749"># 903749</div><div class="band" style="background:#53354a"># 53354A</div><p>Pallet 01</p>
      </div>
      <div class="curated-card">
        <div class="band" style="background:#287294"># 287294</div><div class="band" style="background:#3aa0cf"># 3AA0CF</div><div class="band" style="background:#033247"># 033247</div><div class="band" style="background:#fb991c"># FB991C</div><p>Pallet 02</p>
      </div>
      <div class="curated-card">
        <div class="band" style="background:#00a7a0"># 00A7A0</div><div class="band" style="background:#acd6b1"># ACD6B1</div><div class="band" style="background:#ffca8b"># FFCA8B</div><div class="band" style="background:#ea914f"># EA914F</div><p>Pallet 03</p>
      </div>
    </div>
    <nav class="tabs"><span class="active">Popular</span><span>Trending</span><span>Favourite</span></nav>
    <div class="palette-item"><div class="swatches"><span style="background:#ffc9ae"></span><span style="background:#ffab99"></span><span style="background:#e2959a"></span><span style="background:#b4838c"></span><span style="background:#6b6178"></span></div><div class="item-meta"><span>New Pallete</span><span>♡ 25</span></div></div>
    <div class="palette-item"><div class="swatches"><span style="background:#222441"></span><span style="background:#4a4d6c"></span><span style="background:#9a8a98"></span><span style="background:#cdada6"></span><span style="background:#ecdcd8"></span></div><div class="item-meta"><span>New Pallete</span><span>♡ 25</span></div></div>
    <div class="palette-item"><div class="swatches"><span style="background:#f8e3b5"></span><span style="background:#ffb703"></span><span style="background:#e07f4f"></span><span style="background:#dc5f5d"></span><span style="background:#283753"></span></div><div class="item-meta"><span>New Pallete</span><span>♡ 25</span></div></div>
    <div class="palette-item"><div class="swatches"><span style="background:#71cde0"></span><span style="background:#a5e4dc"></span><span style="background:#e6ecec"></span><span style="background:#e9c6d6"></span><span style="background:#d89bc0"></span></div><div class="item-meta"><span>New Pallete</span><span>♡ 25</span></div></div>
  </div>
  <nav class="tabbar" aria-label="Main">
    <div class="tab home"><svg width="20" height="20" viewBox="0 0 20 20" fill="currentColor"><path d="M10 2 2 9v9h5v-5h6v5h5V9z"/></svg></div>
    <div class="tab"><svg width="20" height="20" viewBox="0 0 20 20" fill="none" stroke="currentColor" stroke-width="1.5"><circle cx="10" cy="10" r="8"/><path d="M2 10h16M10 2c3 3 3 13 0 16M10 2c-3 3-3 13 0 16"/></svg></div>
    <div class="tab"><svg width="20" height="20" viewBox="0 0 20 20" fill="none" stroke="currentColor" stroke-width="1.5"><rect x="2" y="2" width="16" height="16" rx="3"/><path d="M10 6v8M6 10h8"/></svg></div>
    <div class="tab"><svg width="20" height="20" viewBox="0 0 20 20" fill="none" stroke="currentColor" stroke-width="1.5"><path d="M10 17 3 10a4 4 0 0 1 7-5 4 4 0 0 1 7 5z"/></svg></div>
    <div class="tab"><svg width="20" height="20" viewBox="0 0 20 20" fill="none" stroke="currentColor" stroke-width="1.5"><path d="M10 2a8 8 0 1 1-4 15l-4 1 1-4a8 8 0 0 1 7-12z"/></svg><span class="badge">3</span></div>
  </nav>
</section>

<!-- Single palette -->
<section class="screen detail">
  <div class="content">
    <header class="topbar">
      <div class="brand"><span class="brand-dot"></span>Orbitone</div>
      <div class="top-actions">
        <svg class="icon" width="16" height="16" viewBox="0 0 16 16"><circle cx="8" cy="8" r="7" fill="none" stroke="var(--ink)" stroke-width="1.3"/><circle cx="8" cy="8" r="3" fill="var(--ink)"/></svg>
        <svg class="icon" width="16" height="12" viewBox="0 0 16 12" stroke="var(--ink)" stroke-width="1.3"><path d="M0 2h16M0 6h16M0 10h16"/></svg>
      </div>
    </header>
    <h1 class="page-title"><svg width="18" height="12" viewBox="0 0 18 12" fill="none" stroke="var(--ink)" stroke-width="1.5"><path d="M17 6H1M6 1 1 6l5 5"/></svg>Palette 01</h1>
    <div class="colour-list">
      <div class="colour-row" style="background:#b8bede"><span class="round-btn">≡</span><div>#B8BEDE<br>RGB (184,190,222)</div><span class="round-btn">–</span></div>
      <div class="colour-row faded" style="background:#f0e6ee"><span class="round-btn">≡</span><div>#F0E6EE<br>RGB (240,230,238)</div><span class="round-btn">–</span></div>
      <div class="colour-row" style="background:#efc3e6"><span class="round-btn">≡</span><div>#EFC3E6<br>RGB (239,195,230)</div><span class="round-btn">–</span></div>
      <div class="colour-row" style="background:#f0a6ca"><span class="round-btn">≡</span><div>#F0A6CA<br>RGB (240,166,202)</div><span class="round-btn">–</span></div>
      <div class="colour-row" style="background:#9c89b8"><span class="round-btn">≡</span><div>#9C89B8<br>RGB (156,137,184)</div><span class="round-btn">–</span></div>
    </div>
    <div class="add-row" aria-label="Add colour"><svg width="22" height="22" viewBox="0 0 22 22" fill="none" stroke="var(--ink)" stroke-width="1.3"><circle cx="11" cy="11" r="10"/><path d="M11 6v10M6 11h10"/></svg></div>
    <div class="primary-btn"><svg width="12" height="13" viewBox="0 0 12 13" fill="none" stroke="#fff" stroke-width="1.2"><rect x="3" y="3" width="8" height="9"/><path d="M1 10V1h7"/></svg>Copy Palette</div>
  </div>
  <nav class="tabbar" aria-label="Main">
    <div class="tab home"><svg width="20" height="20" viewBox="0 0 20 20" fill="currentColor"><path d="M10 2 2 9v9h5v-5h6v5h5V9z"/></svg></div>
    <div class="tab"><svg width="20" height="20" viewBox="0 0 20 20" fill="none" stroke="currentColor" stroke-width="1.5"><circle cx="10" cy="10" r="8"/><path d="M2 10h16M10 2c3 3 3 13 0 16M10 2c-3 3-3 13 0 16"/></svg></div>
    <div class="tab"><svg width="20" height="20" viewBox="0 0 20 20" fill="none" stroke="currentColor" stroke-width="1.5"><rect x="2" y="2" width="16" height="16" rx="3"/><path d="M10 6v8M6 10h8"/></svg></div>
    <div class="tab"><svg width="20" height="20" viewBox="0 0 20 20" fill="none" stroke="currentColor" stroke-width="1.5"><path d="M10 17 3 10a4 4 0 0 1 7-5 4 4 0 0 1 7 5z"/></svg></div>
    <div class="tab"><svg width="20" height="20" viewBox="0 0 20 20" fill="none" stroke="currentColor" stroke-width="1.5"><path d="M10 2a8 8 0 1 1-4 15l-4 1 1-4a8 8 0 0 1 7-12z"/></svg><span class="badge">3</span></div>
  </nav>
</section>

<!-- Import -->
<section class="screen import">
  <div class="content">
    <header class="topbar">
      <div class="brand"><span class="brand-dot"></span>Orbitone</div>
      <div class="top-actions">
        <svg class="icon" width="16" height="16" viewBox="0 0 16 16"><circle cx="8" cy="8" r="7" fill="none" stroke="var(--ink)" stroke-width="1.3"/><circle cx="8" cy="8" r="3" fill="var(--ink)"/></svg>
        <svg class="icon" width="16" height="12" viewBox="0 0 16 12" stroke="var(--ink)" stroke-width="1.3"><path d="M0 2h16M0 6h16M0 10h16"/></svg>
      </div>
    </header>
    <h1 class="page-title"><svg width="18" height="12" viewBox="0 0 18 12" fill="none" stroke="var(--ink)" stroke-width="1.5"><path d="M17 6H1M6 1 1 6l5 5"/></svg>Import Palette</h1>
    <div class="upload"><div class="upload-core"><svg width="26" height="36" viewBox="0 0 26 36" fill="#fff"><path d="M13 0 0 14h8v12h10V14h8z"/><rect x="8" y="28" width="10" height="2"/><rect x="8" y="32" width="10" height="2"/></svg></div></div>
    <p class="hint">For faster upload or multiple files, compress in<br>ZIP format.</p>
    <div class="file-row"><span class="file-icon"><svg width="11" height="11" viewBox="0 0 11 11" fill="none" stroke="#fff"><rect x="1" y="1" width="9" height="9"/><path d="M1 9l3-3 2 2 2-2 2 2"/></svg></span><div class="file-info">My Images<small>200 MB</small></div><span class="status ok"><svg width="9" height="9" viewBox="0 0 9 9" fill="none" stroke="#fff" stroke-width="1.5"><path d="M1 5l2 2 5-5"/></svg></span></div>
    <div class="file-row"><span class="file-icon"><svg width="11" height="11" viewBox="0 0 11 11" fill="none" stroke="#fff"><rect x="1" y="1" width="9" height="9"/><path d="M1 9l3-3 2 2 2-2 2 2"/></svg></span><div class="file-info">My Documents<small>400 MB</small></div><span class="status ok"><svg width="9" height="9" viewBox="0 0 9 9" fill="none" stroke="#fff" stroke-width="1.5"><path d="M1 5l2 2 5-5"/></svg></span></div>
    <div class="file-row"><span class="file-icon"><svg width="11" height="11" viewBox="0 0 11 11" fill="none" stroke="#fff"><rect x="1" y="1" width="9" height="9"/><path d="M1 9l3-3 2 2 2-2 2 2"/></svg></span><div class="file-info">My Images<small>200 MB</small></div><span class="status bad"><svg width="8" height="8" viewBox="0 0 8 8" fill="none" stroke="#fff" stroke-width="1.5"><path d="M1 1l6 6M7 1 1 7"/></svg></span></div>
    <div class="primary-btn">Import</div>
  </div>
  <nav class="tabbar" aria-label="Main">
    <div class="tab home"><svg width="20" height="20" viewBox="0 0 20 20" fill="currentColor"><path d="M10 2 2 9v9h5v-5h6v5h5V9z"/></svg></div>
    <div class="tab"><svg width="20" height="20" viewBox="0 0 20 20" fill="none" stroke="currentColor" stroke-width="1.5"><circle cx="10" cy="10" r="8"/><path d="M2 10h16M10 2c3 3 3 13 0 16M10 2c-3 3-3 13 0 16"/></svg></div>
    <div class="tab"><svg width="20" height="20" viewBox="0 0 20 20" fill="none" stroke="currentColor" stroke-width="1.5"><rect x="2" y="2" width="16" height="16" rx="3"/><path d="M10 6v8M6 10h8"/></svg></div>
    <div class="tab"><svg width="20" height="20" viewBox="0 0 20 20" fill="none" stroke="currentColor" stroke-width="1.5"><path d="M10 17 3 10a4 4 0 0 1 7-5 4 4 0 0 1 7 5z"/></svg></div>
    <div class="tab"><svg width="20" height="20" viewBox="0 0 20 20" fill="none" stroke="currentColor" stroke-width="1.5"><path d="M10 2a8 8 0 1 1-4 15l-4 1 1-4a8 8 0 0 1 7-12z"/></svg><span class="badge">3</span></div>
  </nav>
</section>

</body>
</html>
```